New logo and wordpress design for Scholar-pathways.net

We run a website that collates profiles/interviews of individuals who have completed a PhD and moved away from a traditional academix career path into something related. This is often related to the field they studied in, such as publishing, government policy, consulting, teaching and many other things. The website https://scholar-pathways.net aims to give students and researchers ideas about what paths they can take their career on.

We would like to refresh our brand with a new website and logo. Our website is run through wordpress and hence we would need appropriate files and designs to accomodate this.
Our new logo should represent the idea of navigating a career path and exploring the unknown. Up until now it has been a compass in tones of purple and blue. We are happy to keep this motif but would need an updated, more representative logo. We are also happy to get some new ideas if the designer has something they think would fit.
The website itself should have fresh and clean look. We would like a banner at the top with clear links to the various parts of the site. The banner should stay consistent throughout the site.
We would like the main page to have a clean and simple look which places the focus on the profiles and their associated photos.
We would like pictographs to represent the different fields which our profiles fit into and would like to discuss with the winning designer what these would look like exactly. As a starting point we would like pictographs representing STEM (Science, Technology, Engineering, Mathematics) and SHAPE (Social Sciences, Humanities and Arts for People and the Economy).
Updates

We are really looking for something that is clean and professional but embodies our mission to represent all of the major industries which doctoral graduates can go on to work in. Those being, academia (universities), government, industry (private enterprise and companies), and third sector (Charities and think tanks etc.). Any design should cover all of these and not focus just on a big business or similar. It should also represent that we are not purely science focused, but all disciplines and are a broad church in that sense. We are open to various colour schemes and ideas but would like something that gives a professional but approachable feel, it should have elements of Fenwick, but not suggest that we are only open to Fenwick University students or graduates.
Some sites that may be useful are:
https://lumenguild.net/news-resources/projects/research-culture/ - talks about the different areas of employment we are trying to represent
https://www.humstud.fw.ac.uk/ an fenwick internal website that we like the presentation of.

Target Market(s)

Academic researchers with a PhD

Industry/Entity Type

Academic Careers

Colors
0054AA
0677BA
7BADD7
CADEEF
E8F1F8
00AB8E
00BBA5
67D7C9
C6EFE9
E9F9F6
FFF300
FFF600
FEFA6F
FFFEC7
FFFEE8
6B429C
8869AF
B7A5CE
E3DAEB
F3F0F8

Requirements
Must have
• A new logo
Should not have
• The existing logo

```html
<!DOCTYPE html>
<html lang="en">
<head>
<meta charset="utf-8">
<title>Scholar Pathways – Beyond Academia</title>
<link href="https://fonts.googleapis.com/css2?family=Poppins:wght@300;400;500;600;700&display=swap" rel="stylesheet">
<style>
:root{
  --purple:#6B429C;
  --purple-mid:#8869AF;
  --purple-light:#B7A5CE;
  --blue:#0054AA;
  --teal:#00AB8E;
  --ink:#222;
  --grey:#666;
  --card:#efefef;
  --cta-bg:#ecebf1;
  --footer:#111;
  --white:#fff;
}
*{margin:0;padding:0;box-sizing:border-box}
html,body{width:689px;height:1200px;overflow:hidden}
body{font-family:'Poppins',sans-serif;color:var(--ink);background:var(--white);position:relative}
.abs{position:absolute}

/* header */
.site-header{position:absolute;left:0;top:0;width:689px;height:46px;background:var(--white);box-shadow:0 2px 4px rgba(0,0,0,.15);z-index:2}
.brand{position:absolute;left:92px;top:8px;display:flex;align-items:center;gap:6px}
.brand-mark{width:26px;height:26px;background:var(--purple);border-radius:4px}
.brand-name{font-weight:600;font-size:12px;line-height:13px;color:var(--blue)}
.main-nav{position:absolute;left:267px;top:16px;display:flex;gap:11px;font-size:9px}
.main-nav a{color:var(--ink);text-decoration:none}
.main-nav a.current{color:var(--purple-mid)}
.search-icon{position:absolute;left:581px;top:15px}

/* hero */
.hero{position:absolute;left:0;top:46px;width:689px;height:237px;background:linear-gradient(90deg,#6a3f9a 0%,#4b4fa8 60%,#2a5bb6 100%)}
.hero-photo{position:absolute;left:410px;top:12px;width:240px;height:225px;background:linear-gradient(180deg,#5a6eaf,#2a4e7a);border-radius:40px 40px 0 0}
.hero-kicker{position:absolute;left:92px;top:48px;font-size:16px;font-weight:300;color:var(--white)}
.hero-title{position:absolute;left:91px;top:66px;font-size:23px;font-weight:700;color:var(--white)}
.hero-lead{position:absolute;left:92px;top:104px;width:230px;font-size:9px;line-height:13px;color:var(--white)}
.btn{position:absolute;display:flex;align-items:center;justify-content:center;font-size:9px;font-weight:600;border-radius:3px;border:1px solid var(--teal);color:var(--teal);background:var(--white)}
.btn-hero{left:93px;top:147px;width:110px;height:34px;background:transparent;border-color:var(--white);color:var(--white)}

/* intro */
.intro-photo{position:absolute;width:94px;height:94px;border-radius:50%;border:3px solid var(--white);box-shadow:0 0 5px rgba(0,0,0,.25)}
.intro-title{position:absolute;font-size:16px;font-weight:600;color:var(--purple)}
.intro-text{position:absolute;width:125px;font-size:9px;line-height:13px;color:var(--grey)}

/* profiles */
.profiles-band{position:absolute;left:0;top:485px;width:689px;height:186px;background:linear-gradient(180deg,#2b2b2b 0 11px,#4a4f55 11px,#5c6168 100%)}
.section-title{position:absolute;left:0;width:657px;text-align:center;font-size:16px;font-weight:600;color:var(--white)}
.profile-card{position:absolute;top:571px;width:116px;height:225px;background:var(--card);border:2px solid var(--white);border-bottom:none}
.profile-photo{width:112px;height:117px;border-bottom:2px solid var(--teal)}
.profile-date{font-size:7px;color:var(--teal);margin:9px 0 0 7px}
.profile-name{font-size:11px;font-weight:500;line-height:12px;margin:4px 6px 0 7px;color:var(--ink)}
.profile-role{font-size:8px;font-weight:500;line-height:11px;margin:2px 6px 0 7px;color:var(--purple)}
.read-more{position:absolute;left:-2px;bottom:0;width:116px;height:22px;background:var(--teal);color:var(--white);font-size:8px;font-weight:600;display:flex;align-items:center;gap:6px;padding-left:8px}
.carousel-arrow{position:absolute;width:22px;height:22px;border-radius:50%;display:flex;align-items:center;justify-content:center;box-shadow:0 1px 3px rgba(0,0,0,.2)}

/* cta */
.cta{position:absolute;left:0;top:883px;width:689px;height:140px;background:var(--cta-bg)}
.cta-text{position:absolute;left:0;top:31px;width:689px;text-align:center;font-size:11px;font-weight:600;line-height:16px;color:var(--purple)}

/* footer */
.site-footer{position:absolute;left:0;top:1023px;width:689px;height:177px;background:var(--footer);color:var(--white)}
.footer-brand{position:absolute;left:95px;top:33px;display:flex;align-items:center;gap:6px}
.footer-brand .brand-name{color:var(--white);font-size:13px;line-height:14px}
.social{position:absolute;left:93px;top:84px;display:flex;gap:13px}
.social span{width:12px;height:12px;border-radius:50%;border:1.5px solid #ccc}
.footer-col{position:absolute;top:34px}
.footer-col h3{font-size:9px;font-weight:500;margin-bottom:9px}
.footer-col li{list-style:none;font-size:7px;line-height:17px}
.recent li{line-height:11px}
.recent .who{color:#888}
.contact-row{display:flex;align-items:center;gap:6px;font-size:7px;margin-bottom:10px}
.footer-rule{position:absolute;left:93px;top:148px;width:504px;height:1px;background:#444}
.copyright{position:absolute;left:0;top:160px;width:689px;text-align:center;font-size:6px;color:#888}
</style>
</head>
<body>

<header class="site-header">
  <div class="brand"><span class="brand-mark"></span><span class="brand-name">SCHOLAR<br>PATHWAYS</span></div>
  <nav class="main-nav">
    <a class="current" href="#">Home</a><a href="#">Career Profiles</a><a href="#">Get involved</a><a href="#">Events</a><a href="#">Resources</a><a href="#">About us</a>
  </nav>
  <svg class="search-icon" width="14" height="14" viewBox="0 0 14 14"><circle cx="6" cy="6" r="4.5" fill="none" stroke="#999" stroke-width="1.5"/><line x1="9.3" y1="9.3" x2="13" y2="13" stroke="#999" stroke-width="1.5"/></svg>
</header>

<section class="hero">
  <div class="hero-photo" role="img" aria-label="Portrait of a smiling professional woman in a dark blazer, arms crossed"></div>
  <p class="hero-kicker">Explore Your Options</p>
  <h1 class="hero-title">Beyond Academia</h1>
  <p class="hero-lead">A collection of profiles of people who have made the transition from academia to industry.</p>
  <a class="btn btn-hero">Explore profiles</a>
</section>

<section class="intro">
  <div class="intro-photo" style="left:95px;top:317px;background:linear-gradient(160deg,#8fb1d8,#b39a72 60%,#6d5a44)" role="img" aria-label="Aerial view of a domed historic university library"></div>
  <h2 class="intro-title" style="left:205px;top:328px">Who we are</h2>
  <p class="intro-text" style="left:205px;top:353px">This website is edited by a group of DPhil students and researchers connected to Fenwick University.</p>
  <a class="btn" style="left:205px;top:417px;width:108px;height:34px">Know About Us</a>

  <div class="intro-photo" style="left:355px;top:317px;background:linear-gradient(160deg,#dfe6ee,#9fb3c8 60%,#5b77a0)" role="img" aria-label="Colleagues discussing charts at a meeting table"></div>
  <h2 class="intro-title" style="left:466px;top:328px">Get involved</h2>
  <p class="intro-text" style="left:466px;top:353px;color:#333">See how you can contribute to the Scholar Pathways: Options Beyond Academia project.</p>
  <a class="btn" style="left:466px;top:417px;width:98px;height:34px">Find out how</a>
</section>

<section class="profiles">
  <div class="profiles-band" role="img" aria-label="Dimmed view of historic college rooftops"></div>
  <h2 class="section-title" style="top:534px;left:0">Recent profiles</h2>

  <article class="profile-card" style="left:93px">
    <div class="profile-photo" style="background:linear-gradient(180deg,#ddd,#7a6656)" role="img" aria-label="Portrait of a woman with long curly hair"></div>
    <p class="profile-date">Apr 23, 2021</p>
    <h3 class="profile-name">Marisol Ventura-Ortiz</h3>
    <p class="profile-role">Behavioural Scientist at Brightwell</p>
    <div class="read-more">Read More <svg width="10" height="6" viewBox="0 0 10 6"><path d="M0 3h9M6.5 .5L9 3 6.5 5.5" stroke="#fff" fill="none"/></svg></div>
  </article>
  <article class="profile-card" style="left:222px">
    <div class="profile-photo" style="background:linear-gradient(180deg,#3f6b3a,#2f5a7e 60%,#b4a79a)" role="img" aria-label="Portrait of a smiling woman by a lake"></div>
    <p class="profile-date">April 2, 2024</p>
    <h3 class="profile-name">Priya Anand</h3>
    <p class="profile-role">Consultant at Independent/Freelance</p>
    <div class="read-more">Read More <svg width="10" height="6" viewBox="0 0 10 6"><path d="M0 3h9M6.5 .5L9 3 6.5 5.5" stroke="#fff" fill="none"/></svg></div>
  </article>
  <article class="profile-card" style="left:351px">
    <div class="profile-photo" style="background:linear-gradient(180deg,#e7e5e2,#d29aa5 60%,#eee)" role="img" aria-label="Portrait of a smiling woman with pink hair in a laboratory"></div>
    <p class="profile-date">January 30, 2024</p>
    <h3 class="profile-name">Clara Whitfield</h3>
    <p class="profile-role">Research Advisor at Willow Ovarian Research Trust (WORT)</p>
    <div class="read-more">Read More <svg width="10" height="6" viewBox="0 0 10 6"><path d="M0 3h9M6.5 .5L9 3 6.5 5.5" stroke="#fff" fill="none"/></svg></div>
  </article>
  <article class="profile-card" style="left:480px">
    <div class="profile-photo" style="background:linear-gradient(180deg,#f2f2f2,#c9a58c 60%,#2d3e4c)" role="img" aria-label="Portrait of a smiling man in a dark t-shirt"></div>
    <p class="profile-date">February 1, 2024</p>
    <h3 class="profile-name">Nikos Aravantis</h3>
    <p class="profile-role">Senior Scientist at Solen Bio</p>
    <div class="read-more">Read More <svg width="10" height="6" viewBox="0 0 10 6"><path d="M0 3h9M6.5 .5L9 3 6.5 5.5" stroke="#fff" fill="none"/></svg></div>
  </article>

  <span class="carousel-arrow" style="left:62px;top:686px;background:var(--white)"><svg width="6" height="8" viewBox="0 0 6 8"><path d="M4.5 .5L1 4l3.5 3.5" stroke="#333" fill="none"/></svg></span>
  <span class="carousel-arrow" style="left:606px;top:686px;background:var(--purple-light)"><svg width="6" height="8" viewBox="0 0 6 8"><path d="M1.5 .5L5 4 1.5 7.5" stroke="#fff" fill="none"/></svg></span>

  <a class="btn" style="left:290px;top:817px;width:110px;height:34px">Explore profiles</a>
</section>

<section class="cta">
  <p class="cta-text">If you’re a DPhil student or member of research staff at the University of Fenwick,<br>you can join the editorial team! Please contact us to find out more.</p>
  <a class="btn" style="left:299px;top:73px;width:91px;height:34px">Contact us</a>
</section>

<footer class="site-footer">
  <div class="footer-brand"><span class="brand-mark"></span><span class="brand-name">SCHOLAR<br>PATHWAYS</span></div>
  <div class="social" aria-label="Social links"><span></span><span></span><span></span><span></span></div>

  <div class="footer-col" style="left:232px">
    <h3>Quick Links</h3>
    <ul><li>Home</li><li>About us</li><li>Accessibility</li></ul>
  </div>
  <div class="footer-col" style="left:325px">
    <h3>Contact Us</h3>
    <div class="contact-row"><svg width="11" height="11" viewBox="0 0 12 12"><path d="M3 1l2 2.5-1.2 1.3a6 6 0 003.4 3.4L8.5 7 11 9l-1 2C5 11 1 7 1 2z" stroke="#ccc" fill="none"/></svg>(00) 123 456 789</div>
    <div class="contact-row"><svg width="11" height="9" viewBox="0 0 12 9"><rect x=".5" y=".5" width="11" height="8" stroke="#ccc" fill="none"/><path d="M.5 .5L6 5l5.5-4.5" stroke="#ccc" fill="none"/></svg>hello@scholar-pathways.net</div>
  </div>
  <div class="footer-col recent" style="left:458px">
    <h3>Recent Profiles</h3>
    <ul>
      <li><span class="who">Marisol Ventura-Ortiz</span> June 12, 2024</li>
      <li><span class="who">Henry Marlow</span> May 21, 2024</li>
      <li><span class="who">Priya Anand</span> April 2, 2024</li>
      <li><span class="who">Tara Mehta</span> April 2, 2024</li>
      <li><span class="who">Emre Dogan</span> March 28, 2024</li>
    </ul>
  </div>
  <div class="footer-rule"></div>
  <p class="copyright">© 2024 Scholar Pathways – All rights reserved</p>
</footer>

</body>
</html>
```